KelvrasMassage website required

We need a website for a mobile sports massage therapist in the United Kingdom. Specialising in pregnancy and postnatal massage, sports and remedial, deep tissue massage & Corprate Massage. Attached are some logos that we already have in various colours. The file named logo_white_background is what we normally use. Feel free to use the others at your discretion.

Requirements
Must have
• Service areas, Booking system.

```html
<!DOCTYPE html>
<html lang="en">
<head>
<meta charset="utf-8">
<title>Kelvra's Massage – Mobile Therapist</title>
<link rel="stylesheet" href="https://fonts.googleapis.com/css2?family=Poppins:wght@400;500;600;700&family=Open+Sans:ital,wght@0,400;0,600;1,400&display=swap">
<style>
:root{
  --teal:#1d6185;
  --sky:#6cc6f4;
  --ink:#3a3a3a;
  --grey-panel:#7a7a7a;
  --footer:#646464;
  --white:#ffffff;
  --card-shadow:0 4px 18px rgba(0,0,0,.10);
}
*{box-sizing:border-box;margin:0;padding:0}
html,body{width:1200px;height:3416px;overflow:hidden}
body{position:relative;font-family:"Open Sans",Arial,sans-serif;color:var(--ink);background:var(--white)}
.abs{position:absolute}
h2.section-title{position:absolute;left:0;width:1200px;text-align:center;font-family:"Poppins",Arial,sans-serif;font-weight:600;font-size:27px;letter-spacing:3px;color:var(--teal)}
.lead{position:absolute;text-align:center;font-size:15px;line-height:26px;color:#333}
.btn{position:absolute;display:flex;align-items:center;justify-content:center;background:var(--sky);color:var(--white);border-radius:20px;font-family:"Poppins",Arial,sans-serif;font-size:12px;white-space:nowrap}

/* hero */
.hero{left:0;top:0;width:1200px;height:676px;background:linear-gradient(115deg,#b48b6b 0%,#d7b396 35%,#e9d2bd 55%,#c9a687 80%,#a98164 100%)}
.hero::after{content:"";position:absolute;inset:0;background:rgba(80,45,20,.12)}
.brand{position:absolute;font-family:"Poppins",Arial,sans-serif;font-weight:600;color:var(--white);text-align:center;line-height:1.1}
.nav a{position:absolute;top:38px;font-family:"Poppins",Arial,sans-serif;font-size:12px;color:var(--white);text-decoration:none;white-space:nowrap}
.hero-kicker{left:200px;width:370px;text-align:center;font-family:"Poppins",Arial,sans-serif;color:var(--white);white-space:nowrap}
.booking{left:713px;top:212px;width:275px;height:378px;background:var(--grey-panel);z-index:2}
.booking h3{position:absolute;top:28px;width:100%;text-align:center;font-family:"Poppins",Arial,sans-serif;font-weight:500;font-size:15px;letter-spacing:2px;color:var(--white)}
.field{position:absolute;left:16px;width:240px;height:31px;background:var(--white);border-radius:3px;font-size:10.5px;color:#666;padding:8px 10px}

/* services */
.services-band{left:0;top:1123px;width:1200px;height:373px;background:linear-gradient(100deg,#9a6a45 0%,#c48a5c 40%,#d9a878 65%,#b88a6a 100%)}
.services-band::after{content:"";position:absolute;inset:0;background:rgba(50,25,10,.25)}
.service-card{top:1391px;height:283px;background:var(--white);box-shadow:var(--card-shadow);z-index:2;text-align:center}
.service-icon{position:absolute;left:50%;top:40px;width:36px;height:36px;margin-left:-18px;border-radius:8px;background:#cdebfb}
.service-card h4{position:absolute;left:0;top:110px;width:100%;font-family:"Poppins",Arial,sans-serif;font-weight:600;font-size:13px;color:var(--teal)}
.service-card p{position:absolute;top:140px;left:20px;right:20px;font-size:9.5px;line-height:14px;color:#555}
.price{position:absolute;left:0;bottom:0;width:100%;height:57px;background:var(--sky);color:var(--white);font-family:"Poppins",Arial,sans-serif;display:flex;align-items:center;justify-content:center;gap:4px}
.price strong{font-size:22px;font-weight:600}.price span{font-size:12px}

/* about */
.about-band{left:0;top:1829px;width:1200px;height:437px;background:linear-gradient(90deg,#cfc8bf 0%,#e2dcd3 35%,#b7a37d 60%,#7e7150 80%,#cfd3d0 100%)}
.about-band::after{content:"";position:absolute;inset:0;background:rgba(60,50,40,.35)}
.rule{left:0;width:1200px;height:6px;background:var(--sky)}
.badge{width:64px;height:64px;border-radius:50%;background:var(--white);left:568px;display:flex;align-items:center;justify-content:center;z-index:3}
.badge i{display:block;width:30px;height:30px;border-radius:50%;background:var(--teal)}

/* stats */
.stat{top:2368px;height:153px;width:184px;background:var(--white);box-shadow:var(--card-shadow);text-align:center;font-family:"Poppins",Arial,sans-serif}
.stat b{position:absolute;left:0;top:22px;width:100%;font-size:46px;line-height:60px;font-weight:600;color:var(--teal)}
.stat span{position:absolute;left:0;top:94px;width:100%;font-size:13px;font-weight:500;color:#333;white-space:nowrap}

/* reviews */
.review{top:2767px;height:220px;width:250px;background:var(--white);box-shadow:var(--card-shadow)}
.avatar{position:absolute;left:90px;top:4px;width:68px;height:68px;border-radius:50%;background:linear-gradient(160deg,#6b3a36,#a2302f);border:3px solid #eee}
.stars{position:absolute;left:160px;top:58px;font-size:11px;letter-spacing:1px;color:var(--sky)}
.review p{position:absolute;top:98px;left:20px;right:20px;font-style:italic;font-size:10.5px;line-height:16px;text-align:center;color:#555}
.review .name{position:absolute;right:18px;top:172px;font-family:"Poppins",Arial,sans-serif;font-size:13px;color:#333;text-align:right}
.review .role{position:absolute;right:18px;top:189px;font-style:italic;font-size:11px;color:#555}
.dot{top:3036px;width:10px;height:10px;border-radius:50%;border:1.5px solid var(--sky)}

/* footer */
.footer{left:0;top:3133px;width:1200px;height:283px;background:var(--footer);color:var(--white)}
.footer h5{position:absolute;top:82px;font-family:"Poppins",Arial,sans-serif;font-weight:500;font-size:11px;letter-spacing:1px}
.footer ul{position:absolute;top:110px;list-style:none;font-size:9px;line-height:18.5px;white-space:nowrap}
.contact-row{position:absolute;left:545px;display:flex;gap:10px;font-size:8.5px;line-height:12px;align-items:flex-start}
.contact-row svg{flex:none}
.social{position:absolute;top:3337px;width:28px;height:28px;border-radius:50%;background:var(--sky)}
.copy{position:absolute;top:3394px;left:0;width:1200px;text-align:center;font-size:8.5px;color:var(--white)}
</style>
</head>
<body>

<!-- HERO -->
<section class="abs hero" role="img" aria-label="Photo of a therapist giving a relaxing head massage to a woman lying on a treatment table"></section>
<div class="brand" style="left:200px;top:26px;width:120px;font-size:15px;z-index:2">Kelvra's<br><span style="font-size:8px;letter-spacing:3px">MASSAGE</span></div>
<nav class="nav" style="position:absolute;z-index:2">
  <a href="#" style="left:425px">Home</a>
  <a href="#" style="left:514px">Services ▾</a>
  <a href="#" style="left:612px">About</a>
  <a href="#" style="left:696px">Reviews</a>
  <a href="#" style="left:788px">Contact</a>
</nav>
<a class="btn" style="left:877px;top:32px;width:110px;height:29px;z-index:2;text-decoration:none">Book Now</a>

<div class="abs hero-kicker" style="top:284px;font-size:15px;line-height:20px;letter-spacing:3px;z-index:2">MOBILE THERAPIST</div>
<h1 class="abs hero-kicker" style="top:304px;font-size:60px;line-height:62px;font-weight:600;letter-spacing:4px;z-index:2">MASSAGE</h1>
<div class="abs hero-kicker" style="top:368px;font-size:12px;line-height:16px;letter-spacing:10px;z-index:2">UNITED KINGDOM</div>

<form class="abs booking">
  <h3>BOOKING FORM</h3>
  <div class="field" style="top:75px">Full Name</div>
  <div class="field" style="top:123px">Email</div>
  <div class="field" style="top:171px">Phone Number</div>
  <div class="field" style="top:220px">Appointment Date (dd/mm/yyyy)</div>
  <div class="field" style="top:268px">Requested Services <span style="float:right;color:var(--sky)">▼</span></div>
  <div class="btn" style="left:82px;top:328px;width:111px;height:27px;font-size:10px">Book Now</div>
</form>

<!-- MOTIVATION -->
<h2 class="section-title" style="top:788px">MY MOTIVATION</h2>
<p class="lead" style="left:305px;top:852px;width:590px">This is Photoshop's version  of Lorem Ipsum. Proin gravida nibh vel velit auctor aliquet. Aenean sollicitudin, lorem quis bibendum auctor, nisi elit consequat ipsum, nec sagittis sem nibh id elit. Duis sed odio sit amet nibh vulputate cursus a sit amet mauris. Morbi accumsan ipsum velit. Nam nec tellus a odio tincidunt auctor a ornare odio. Sed non  mauris vitae erat consequat auctor eu</p>
<div class="abs" role="img" aria-label="Handwritten signature of the therapist" style="left:560px;top:1010px;width:80px;height:56px;border-radius:28px;background:#ececec"></div>

<!-- SERVICES -->
<section class="abs services-band" role="img" aria-label="Photo of a therapist massaging a client's shoulders in a warm-lit room"></section>
<h2 class="abs" style="left:212px;top:1200px;font-family:'Poppins',sans-serif;font-weight:600;font-size:27px;letter-spacing:2px;color:var(--white);z-index:2">MY SERVICES</h2>
<p class="abs" style="left:212px;top:1256px;width:600px;font-size:15px;line-height:26px;color:var(--white);z-index:2">This is Photoshop's version  of Lorem Ipsum. Proin gravida nibh vel velit auctor aliquet. Aenean sollicitudin, lorem quis bibendum auctor, nisi elit consequat ipsum, nec sagittis sem nibh id elit. Duis sed odio sit amet nibh vulputate</p>

<article class="abs service-card" style="left:212px;width:250px">
  <div class="service-icon" role="img" aria-label="Pregnancy icon"></div>
  <h4>Pregnancy &amp; Postnatal</h4>
  <p>This is Photoshop's version of Lorem Ipsum. Proin gravida nibh vel velit auctor aliquet. Aenean sollicitudin, lorem quis bibendum auctor, nisi elit consequat ipsum, nec sagittis sem nibh id elit.</p>
  <div class="price"><strong>£ 25</strong><span>/ Session</span></div>
</article>
<article class="abs service-card" style="left:476px;width:248px">
  <div class="service-icon" role="img" aria-label="Sports massage icon"></div>
  <h4>Sports &amp; Remedial</h4>
  <p>This is Photoshop's version of Lorem Ipsum. Proin gravida nibh vel velit auctor aliquet. Aenean sollicitudin, lorem quis bibendum auctor, nisi elit consequat ipsum, nec sagittis sem nibh id elit.</p>
  <div class="price"><strong>£ 25</strong><span>/ Session</span></div>
</article>
<article class="abs service-card" style="left:738px;width:250px">
  <div class="service-icon" role="img" aria-label="Deep tissue massage icon"></div>
  <h4>Deep Tissue &amp; Corporate</h4>
  <p>This is Photoshop's version of Lorem Ipsum. Proin gravida nibh vel velit auctor aliquet. Aenean sollicitudin, lorem quis bibendum auctor, nisi elit consequat ipsum, nec sagittis sem nibh id elit.</p>
  <div class="price"><strong>£ 25</strong><span>/ Session</span></div>
</article>
<div class="btn" style="left:531px;top:1721px;width:137px;height:32px">Book Now</div>

<!-- ABOUT -->
<section class="abs about-band" role="img" aria-label="Photo of massage oil bottles and dried flowers beside folded white towels"></section>
<h2 class="section-title" style="top:1902px;color:var(--white);z-index:2">ABOUT</h2>
<p class="lead" style="left:305px;top:1960px;width:590px;color:var(--white);z-index:2">This is Photoshop's version  of Lorem Ipsum. Proin gravida nibh vel velit auctor aliquet. Aenean sollicitudin, lorem quis bibendum auctor, nisi elit consequat ipsum, nec sagittis sem nibh id elit. Duis sed odio sit amet nibh vulputate cursus a sit amet mauris. Morbi accumsan ipsum velit. Nam nec tellus a odio tincidunt auctor a ornare odio. Sed non  mauris vitae erat consequat auctor eu</p>
<div class="btn" style="left:531px;top:2141px;width:137px;height:32px;z-index:2">Book Now</div>
<div class="abs rule" style="top:2266px;z-index:2"></div>
<div class="abs badge" style="top:2237px"><i></i></div>

<!-- STATS -->
<div class="abs stat" style="left:212px"><b>3</b><span>Therapist Degree</span></div>
<div class="abs stat" style="left:411px"><b>7</b><span>Massage Programs</span></div>
<div class="abs stat" style="left:610px"><b>321</b><span>Happy Clients</span></div>
<div class="abs stat" style="left:806px"><b>3</b><span>Therapist Degree</span></div>

<!-- REVIEWS -->
<h2 class="section-title" style="top:2594px">REVIEWS</h2>
<p class="lead" style="left:305px;top:2660px;width:590px">This is Photoshop's version  of Lorem Ipsum. Proin gravida nibh vel velit auctor aliquet. Aenean sollicitudin, lorem quis bibendum auctor, nisi elit consequat</p>

<article class="abs review" style="left:212px">
  <div class="avatar" role="img" aria-label="Client portrait"></div><div class="stars">★★★★★</div>
  <p>Lorem ipsum dolor sit amet, consectetur adipisicing elit, sed do eiusmod tempor incididunt ut labore et dolore magna aliqua. Ut enim ad minim veniam, quis nostrud</p>
  <div class="name">Mara Ellison</div><div class="role">Mom and wife</div>
</article>
<article class="abs review" style="left:475px">
  <div class="avatar" role="img" aria-label="Client portrait"></div><div class="stars">★★★★★</div>
  <p>Lorem ipsum dolor sit amet, consectetur adipisicing elit, sed do eiusmod tempor incididunt ut labore et dolore magna aliqua. Ut enim ad minim veniam, quis nostrud</p>
  <div class="name">Mara Ellison</div><div class="role">Mom and wife</div>
</article>
<article class="abs review" style="left:738px">
  <div class="avatar" role="img" aria-label="Client portrait"></div><div class="stars">★★★★★</div>
  <p>Lorem ipsum dolor sit amet, consectetur adipisicing elit, sed do eiusmod tempor incididunt ut labore et dolore magna aliqua. Ut enim ad minim veniam, quis nostrud</p>
  <div class="name">Mara Ellison</div><div class="role">Mom and wife</div>
</article>
<div class="abs dot" style="left:537px;background:var(--sky)"></div>
<div class="abs dot" style="left:566px"></div>
<div class="abs dot" style="left:595px"></div>
<div class="abs dot" style="left:624px"></div>
<div class="abs dot" style="left:653px"></div>

<!-- FOOTER -->
<div class="abs rule" style="top:3126px"></div>
<footer class="abs footer">
  <div class="brand" style="left:250px;top:72px;width:120px;font-size:15px">Kelvra's<br><span style="font-size:8px;letter-spacing:3px">MASSAGE</span></div>
  <p class="abs" style="left:212px;top:120px;width:260px;font-size:8.5px;line-height:13px">This is Photoshop's version of Lorem Ipsum. Proin gravida nibh vel velit auctor aliquet. Aenean sollicitudin, lorem quis bibendum auctor, nisi elit consequat ipsum, nec sagittis sem nibh id elit. Duis sed odio sit amet nibh vulputate cursus a sit amet mauris.</p>

  <h5 style="left:588px">CONTACT</h5>
  <div class="contact-row" style="top:108px">
    <svg width="14" height="14" viewBox="0 0 14 14"><circle cx="7" cy="7" r="7" fill="var(--sky)"/><path d="M4.5 4c.5 2.8 2.5 5 5 5.5l.8-1.2-1.5-.8-.7.6c-.9-.5-1.6-1.2-2-2l.6-.7-.8-1.5z" fill="#fff"/></svg>
    <span>01632 960 184</span></div>
  <div class="contact-row" style="top:136px">
    <svg width="14" height="14" viewBox="0 0 14 14"><rect x="1" y="3" width="12" height="8" rx="1" fill="var(--sky)"/><path d="M1.5 3.5 7 8l5.5-4.5" stroke="#fff" fill="none"/></svg>
    <span>hello@kelvrasmassage.co.uk</span></div>
  <div class="contact-row" style="top:162px">
    <svg width="14" height="16" viewBox="0 0 14 16"><path d="M7 1a5 5 0 0 1 5 5c0 4-5 9-5 9S2 10 2 6a5 5 0 0 1 5-5z" fill="var(--sky)"/><circle cx="7" cy="6" r="2" fill="#fff"/></svg>
    <span>14 Harrow Lane, 2nd Floor,<br>Bristol, BS1 4QX</span></div>
  <div class="contact-row" style="top:196px">
    <svg width="14" height="14" viewBox="0 0 14 14"><rect x="1" y="2" width="12" height="11" rx="1" fill="var(--sky)"/><rect x="3" y="6" width="8" height="5" fill="#fff"/></svg>
    <span>Monday - Friday 8 am to 6 pm</span></div>

  <h5 style="left:744px">SERVICES</h5>
  <ul style="left:730px"><li>Pregnancy Massage</li><li>Postnatal Massage</li><li>Sports Massage</li><li>Remedial Massage</li><li>Deep Tissue Massage</li><li>Corporate Massage</li></ul>

  <h5 style="left:862px">SUPPORT</h5>
  <ul style="left:860px"><li>About Me</li><li>FAQ</li><li>Prices Table</li><li>Guarantee</li><li>Privacy Policy</li><li>Booking Form</li></ul>
</footer>
<div class="abs badge" style="top:3105px"><i></i></div>
<div class="social" style="left:229px"></div>
<div class="social" style="left:265px"></div>
<div class="social" style="left:301px"></div>
<div class="social" style="left:337px"></div>
<div class="social" style="left:373px"></div>
<div class="social" style="left:409px"></div>
<div class="copy">Copyright © 2018, Kelvra's Massage - All rights reserved.</div>

</body>
</html>
```